Local Chiropractor Needs Up Scale Webdesign

This website needs to have an upscale look with a very modern feel. Below is the information and websites to reference

Add Logo that is attached

Build a color scheme similar to this website image titled "chiro-1"

Must Include these pages in a horizontal menu bar in this order:
Home, Meet Our Staff, Patient Testimonials, Videos, Work Place Wellness, Contact

Build a "classy looking" Make An Appointment Button into the header with the contact info below

Phone Number:
555-314-2706

Address:
4318 Willow Barn Lane, #215
Chanhassen, MN 55492

This website needs 4 rotating banners. Please reference a layout similar to this for the banners: http://drkelmora.com/. However design it nicer than this website, this website is very boring and doesn't flow with the colors properly

Below are the description for each banner

Rotating Banner #1
Use Image: Pediatrics
Two lines of text. First line title line, second description. Use Latin text for fill

Rotating Banner #2
Use Image: Aging Gracefully

Rotating Banner #3
Use Image: Pregnancy

Rotating Banner #4
Use Image: Athletics

I'd like to see a free consultation box similar to the "chiro-1" image. Fields to include are: First Name, Last Name, Phone Number, Comments.

For the body, please fill it with latin text. Please design a professional body layout. You can include a box in the right column for the hours

Office Hours
Monday: 8:00-11:00, 2:00-5:00
Tuesday: 8:30-11:00, 2:00-5:30
Wednesday: 8:00-11:00, 2:00-5:00
Thursday: 10:00-12:00, 2:30-5:00
Friday: 8:00-10:00, 1:00-5:00
Saturday: Closed
Sunday: Closed

For the footer please design something similar to the: http://drkelmora.com/

Also include in the Footer: Powered by Tandem Pixel Works

```html
<!DOCTYPE html>
<html lang="en">
<head>
<meta charset="utf-8">
<title>Evergreen Path Chiropractic Health Center</title>
<link href="https://fonts.googleapis.com/css2?family=Questrial&display=swap" rel="stylesheet">
<style>
:root{
  --black:#0c0c0c;
  --green:#74a314;
  --green-dark:#5f8a0c;
  --leaf:#6e9a17;
  --orange:#f5902a;
  --orange-light:#fbb55a;
  --gold:#d79a22;
  --gold-text:#e0a12a;
  --paper:#f7f7f5;
  --band:#f4f4f2;
  --footer:#1f1f1f;
  --ink:#333;
  --muted:#555;
  --white:#fff;
}
*{box-sizing:border-box;margin:0;padding:0}
html,body{width:1109px;height:1200px;overflow:hidden}
body{font-family:"Questrial",Arial,sans-serif;color:var(--ink);background:var(--white);position:relative}
.abs{position:absolute}

.top-bar{left:0;top:0;width:1109px;height:15px;background:var(--black);color:var(--white);font-family:Arial,sans-serif;font-size:7.5px;font-weight:bold;line-height:15px}
.top-bar span{position:absolute;top:0}

.site-header{left:0;top:15px;width:1109px;height:105px;background:var(--paper)}
.brand{position:absolute;left:210px;top:30px;display:flex;align-items:center;gap:8px}
.brand-dot{width:34px;height:34px;border-radius:50%;background:var(--leaf)}
.brand-name{color:var(--leaf);font-size:20px;line-height:1.05}
.brand-name small{display:block;font-size:12.5px}
.appt-btn{position:absolute;left:650px;top:39px;width:243px;height:32px;border-radius:6px;background:linear-gradient(var(--orange-light),var(--orange));box-shadow:0 1px 3px rgba(0,0,0,.25);color:var(--white);font-size:16px;letter-spacing:.3px;display:flex;align-items:center;padding-left:22px;gap:10px}

.main-nav{left:0;top:120px;width:1109px;height:28px;background:var(--green)}
.main-nav ul{list-style:none;position:absolute;left:222px;top:5px;display:flex;gap:0}
.main-nav li{font-size:10.5px;color:var(--white);height:18px;line-height:18px;padding:0 8px;margin-right:5px}
.main-nav li.active{background:var(--orange);padding:0 15px;margin-right:0}

.hero{left:0;top:148px;width:1109px;height:450px;background:linear-gradient(120deg,#e9ecef 0%,#c9d3de 30%,#f1f2f3 55%,#dfe3e6 80%,#eef0f1 100%)}
.hero-title{position:absolute;left:208px;top:332px;font-size:25px;color:#222;letter-spacing:.3px}
.hero-text{position:absolute;left:208px;top:366px;font-size:12px;color:#333;line-height:15.5px}
.dots{position:absolute;left:812px;top:422px;display:flex;gap:7px}
.dots i{width:13px;height:13px;border-radius:50%;background:var(--green)}
.dots i:first-child{background:var(--gold)}

.consult{left:674px;top:205px;width:216px;height:311px;background:rgba(250,250,250,.92);padding:33px 10px 0}
.consult h2{font-weight:normal;font-size:17px;color:#111;padding-left:6px}
.consult h3{font-weight:bold;font-size:9px;color:#111;padding-left:6px;margin-bottom:18px}
.field{height:24px;border:1px solid #d4d4d4;border-radius:2px;background:var(--white);margin-bottom:4px;font-size:9.5px;color:#444;padding:5px 9px}
.field.area{height:72px}
.submit{margin-top:11px;width:90px;height:27px;background:var(--gold);border-radius:2px;color:var(--white);font-size:10px;text-align:center;line-height:27px}

.services{left:0;top:598px;width:1109px;height:114px;background:var(--band);border-bottom:2px solid #e2e2e2}
.service{position:absolute;top:32px;width:150px;text-align:center;color:var(--green);font-size:8.5px}
.service .ring{width:40px;height:40px;border:1px solid var(--green);border-radius:50%;margin:0 auto 13px;display:flex;align-items:center;justify-content:center}

.welcome{left:0;top:760px;width:1109px;text-align:center}
.welcome h1{font-weight:normal;font-size:25px;color:var(--leaf);line-height:28px}
.welcome h2{font-weight:normal;font-size:20px;color:var(--gold);line-height:24px}
.welcome p{width:600px;margin:18px auto 0;font-size:9.5px;line-height:11.8px;color:var(--muted)}

.site-footer{left:0;top:947px;width:1109px;height:212px;background:var(--footer);color:#e5e5e5}
.site-footer h4{position:absolute;top:36px;font-weight:normal;font-size:17px;color:var(--gold-text)}
.contact-row{position:absolute;left:208px;display:flex;gap:10px;font-size:9.5px;line-height:11.5px}
.contact-row svg{flex:none}
.map{position:absolute;left:468px;top:68px;width:173px;height:94px;border:3px solid #999;background:linear-gradient(135deg,#e6e2d6,#d9d5c7 60%,#e9e4d3)}
.hours{position:absolute;left:727px;top:66px;font-size:9.5px;line-height:13.9px;border-collapse:collapse}
.hours td{padding:0}
.hours td:first-child{width:62px}

.bottom-bar{left:0;top:1159px;width:1109px;height:37px;background:var(--green);color:var(--white);font-size:10px;line-height:37px}
.bottom-strip{left:0;top:1196px;width:1109px;height:4px;background:var(--footer)}
</style>
</head>
<body>

<div class="abs top-bar">
  <span style="left:559px">Address: 4318 Willow Barn Lane, #215 Chanhassen, MN 55492</span>
  <span style="left:798px">Phone Number: 555-314-2706</span>
</div>

<header class="abs site-header">
  <div class="brand">
    <span class="brand-dot"></span>
    <span class="brand-name">Evergreen Path<small>Chiropractic Health Center</small></span>
  </div>
  <div class="appt-btn">MAKE AN APPOINTMENT
    <svg width="20" height="20" viewBox="0 0 20 20"><circle cx="10" cy="10" r="9" fill="#7a4a12"/><path d="M5 10h9M10 6l4 4-4 4" stroke="#fff" stroke-width="2" fill="none" stroke-linecap="round"/></svg>
  </div>
</header>

<nav class="abs main-nav">
  <ul>
    <li class="active">Home</li><li>Meet Our Staff</li><li>Patient Testimonials</li><li>Videos</li><li>Work Place Wellness</li><li>Contact</li>
  </ul>
</nav>

<section class="abs hero" role="img" aria-label="Banner photo: two skiers in bright jackets skiing through fresh snow among snowy trees">
  <div class="hero-title">LOROM IPSUM DOLOR SIMET</div>
  <div class="hero-text">Ut enim ad minim veniam, quis nostrud exercitation<br>ullamco laboris nisi ut aliquip ex ea commodo consequat.</div>
  <div class="dots"><i></i><i></i><i></i><i></i></div>
</section>

<form class="abs consult">
  <h2>FREE CONSULTATION</h2>
  <h3>CONTACT US TODAY!</h3>
  <div class="field">First Name</div>
  <div class="field">Last Name</div>
  <div class="field">Phone Number</div>
  <div class="field area">Comments</div>
  <div class="submit">Submit</div>
</form>

<section class="abs services">
  <div class="service" style="left:325px">
    <div class="ring"><svg width="18" height="18" viewBox="0 0 18 18"><path d="M4 14C3 8 8 3 15 3c0 7-5 12-11 11zM4 14l6-6" stroke="#74a314" stroke-width="1.4" fill="none"/></svg></div>
    HEALTH &amp; WELLNESS
  </div>
  <div class="service" style="left:482px">
    <div class="ring"><svg width="18" height="18" viewBox="0 0 18 18"><path d="M9 2c2 3 2 5 0 7-2-2-2-4 0-7zM4 12h10v3H4z" fill="#74a314"/></svg></div>
    THERAPEUTIC TREATMENT
  </div>
  <div class="service" style="left:638px">
    <div class="ring"><svg width="18" height="18" viewBox="0 0 18 18"><ellipse cx="9" cy="14" rx="6" ry="2.2" fill="#74a314"/><ellipse cx="9" cy="10" rx="4.5" ry="2" fill="#74a314"/><ellipse cx="9" cy="6.3" rx="3" ry="1.6" fill="#74a314"/></svg></div>
    MESSAGE THERPAY
  </div>
</section>

<section class="abs welcome">
  <h1>WELCOME TO EVERGREEN PATH</h1>
  <h2>CHIROPRACTIC HEALTH CENTER WEBSITE</h2>
  <p>Lorem ipsum dolor sit amet, consectetur adipiscing elit, sed do eiusmod tempor incididunt ut labore et dolore magna aliqua. Ut enim ad minim veniam, quis nostrud exercitation ullamco laboris nisi ut aliquip ex ea commodo consequat. Duis aute irure dolor in reprehenderit in voluptate velit esse cillum dolore eu fugiat nulla pariatur. Excepteur sint occaecat cupidatat non proident, sunt in culpa qui officia deserunt mollit anim id est laborum.</p>
</section>

<footer class="abs site-footer">
  <h4 style="left:208px">CONTACT US</h4>
  <h4 style="left:467px">GET DIRECTIONS</h4>
  <h4 style="left:726px">OFFICE HOURS</h4>

  <div class="contact-row" style="top:80px">
    <svg width="12" height="14" viewBox="0 0 12 14"><path d="M6 0a5 5 0 0 0-5 5c0 4 5 9 5 9s5-5 5-9a5 5 0 0 0-5-5z" fill="#fff"/><circle cx="6" cy="5" r="2" fill="#1f1f1f"/></svg>
    <span>4318 Willow Barn Lane,<br>#215 Chanhassen, MN 55492</span>
  </div>
  <div class="contact-row" style="top:116px">
    <svg width="12" height="12" viewBox="0 0 12 12"><path d="M2 1l2 0 1 3-1.5 1a6 6 0 0 0 3.5 3.5L8 7l3 1v2c0 1-1 1.5-2 1.5C5 11 1 7 .5 3 .5 2 1 1 2 1z" fill="#fff"/></svg>
    <span>555-314-2706</span>
  </div>
  <div class="contact-row" style="top:138px">
    <svg width="12" height="10" viewBox="0 0 12 10"><rect x="0" y="1" width="12" height="8" fill="#fff"/><path d="M0 1l6 5 6-5" stroke="#1f1f1f" fill="none"/></svg>
    <span>info@evergreenpathchiro.com</span>
  </div>

  <div class="map" role="img" aria-label="Street map showing the clinic location"></div>

  <table class="hours">
    <tr><td>Monday:</td><td>8:00-11:00, 2:00-5:00</td></tr>
    <tr><td>Tuesday:</td><td>8:30-11:00, 2:00-5:30</td></tr>
    <tr><td>Wednesday:</td><td>8:00-11:00, 2:00-5:00</td></tr>
    <tr><td>Thursday:</td><td>10:00-12:00, 2:30-5:00</td></tr>
    <tr><td>Friday:</td><td>8:00-10:00, 1:00-5:00</td></tr>
    <tr><td>Saturday:</td><td>Closed</td></tr>
    <tr><td>Sunday:</td><td>Closed</td></tr>
  </table>
</footer>

<div class="abs bottom-bar">
  <span class="abs" style="left:209px">Copyright ©2015 EvergreenPath. All Rights Reserved.</span>
  <span class="abs" style="right:217px">Powered by Tandem Pixel Works</span>
</div>
<div class="abs bottom-strip"></div>

</body>
</html>
```